Trucking Insurance Website Design

We are working with a Trucking Insurance company in California. They provide vehicle insurance for trucking companies and truckers.
As you might imagine, there are no websites we could find for inspiration for trucking insurance. But below are sites that do similar insurance.
https://brindlemorecover.com/trucking-insurance/
https://www.haulwardpolicy.com/california-commercial-truck-insurance
Thank you for taking the time to consider designing a website for us. We are web developers based in Stockton, CA, USA. Most of our projects go through the same process. Understanding this process may help you win a project with us. We custom-code all of our websites in-house. We don’t have any requirements as to what tools you use for your design, but we ask that you follow these guidelines.
IMAGES:
If you use any images or icons in the design, we ask that you have a link to the asset so we can purchase the image/icon. Most of the designs we submit do not have the customer’s images on them unless they have some great images. Be creative; show us the feeling you are trying to portray with your image choices. Use any royalty-free site you choose. We subscribe to Quillen and mainly use their images, but we can purchase images outside of Quillen. PLEASE NOTE: we will not submit designs to clients with watermarks on the images.
FONTS:
We ask that you identify the fonts you’re using in the design. This can be done in a message if you want. We typically use Marlowe Type and Quillen Type.
CONTENT:
We're always open to different content and ideas. We often submit designs with stock images so the client can see our vision. We typically take pictures after the website launch to use their images with our vision. Lorem Ipsum is fine for paragraphs, but we ask that you make the Headers with correct English. We want to be able to show the vision and identify the sections of the website.
INSPIRATION:
We typically add a couple of links in the brief of websites we like to help you get started in your design.
REVISIONS:
We do not often ask for revisions of the designs unless we see something in the design that may not appeal to the client. If there are slight changes that we want to make, we do that in the development process.
FEEDBACK:
We rarely give feedback on designs during the design process. We are working on many website projects and do not have the time to provide feedback. We usually respond if your request is well thought out and asks specific questions, but a note asking “feedback, please” usually goes unanswered.
1 page

```html
<!DOCTYPE html>
<html lang="en">
<head>
<meta charset="utf-8">
<title>Milepost Insurance – Trucking Insurance</title>
<link rel="stylesheet" href="https://fonts.googleapis.com/css2?family=League+Spartan:wght@500;600;700;800&family=Lato:wght@400;700&family=Quicksand:wght@400;500&display=swap">
<style>
:root{
  --orange:#ff5a0a;
  --navy:#0c3b60;
  --navy-deep:#0a2f4d;
  --teal:#0a4658;
  --ink:#1d1d1d;
  --muted:#444;
  --sky:#eef9fd;
  --mist:#f1f1f1;
  --night:#1a1a1a;
  --footer:#161616;
  --white:#fff;
}
*{margin:0;padding:0;box-sizing:border-box}
html,body{width:1200px;height:5226px;overflow:hidden}
body{position:relative;background:var(--white);font-family:"Lato",sans-serif;color:var(--ink)}
.abs{position:absolute}
h1,h2,h3,.display{font-family:"League Spartan",sans-serif}
.accent{color:var(--orange)}

/* header */
.site-header{left:0;top:0;width:1200px;height:75px;background:var(--white)}
.brand{display:flex;align-items:center;gap:8px;font-family:"League Spartan",sans-serif;font-weight:700;font-size:11px;letter-spacing:2px;color:var(--navy);line-height:1.1}
.brand-dot{width:22px;height:22px;border-radius:50%;background:var(--navy);flex:none}
.main-nav a{position:absolute;top:30px;font-size:12px;font-weight:700;color:var(--ink);text-decoration:none}
.main-nav a.active{color:var(--orange)}
.btn{display:flex;align-items:center;justify-content:center;font-size:12px;font-weight:700;text-decoration:none}
.btn-solid{background:var(--orange);color:var(--white)}
.btn-ghost{border:2px solid var(--white);color:var(--white)}

/* hero */
.hero{left:0;top:75px;width:1200px;height:522px}
.hero-title{left:666px;top:160px;font-size:35px;line-height:37px;font-weight:700;color:var(--white)}
.hero-sub{left:666px;top:286px;width:280px;font-size:11.5px;line-height:18px;color:#dfe8ee}
.stats{left:0;top:597px;width:1200px;height:108px;background:var(--teal)}
.stat{position:absolute;top:22px;color:var(--white)}
.stat b{display:block;font-family:"Quicksand",sans-serif;font-weight:400;font-size:38px;line-height:40px}
.stat span{font-size:11px}

/* about */
.about{left:0;top:705px;width:1200px;height:260px;background:var(--sky);text-align:center}
.section-title{font-size:31px;font-weight:700;color:var(--ink)}
.about p{width:590px;margin:14px auto 0;font-size:11px;line-height:19px;color:var(--muted)}

/* services */
.services-head{left:225px;top:1030px}
.section-sub{font-size:11px;color:var(--muted);margin-top:8px}
.service-photo{width:369px;height:157px}
.service-count{font-size:10px;color:var(--muted)}
.service-title{font-size:17px;font-weight:700;color:var(--ink)}
.service-desc{width:300px;font-size:11px;line-height:19px;color:var(--muted);margin-top:12px}

/* claims */
.claims{left:0;top:2505px;width:1200px;height:1025px;background:var(--mist)}
.center-head{left:0;width:1200px;text-align:center}
.claim-card{width:242px;height:365px;background:var(--white);box-shadow:0 2px 8px rgba(0,0,0,.12);padding:28px 16px 0 16px}
.claim-card.featured{background:var(--navy)}
.claim-card h3{font-size:15px;font-weight:600;margin:14px 0 12px;color:var(--ink)}
.claim-card p{font-size:11px;line-height:19px;color:var(--muted);margin-bottom:19px}
.claim-card.featured h3,.claim-card.featured p{color:var(--white)}

/* testimonials */
.testimonials{left:0;top:3530px;width:1200px;height:625px;background:var(--night);overflow:hidden}
.quote-card{top:190px;height:268px;background:#2a2a2a;padding:28px 32px}
.quote-avatar{width:60px;height:60px;border-radius:50%;background:linear-gradient(135deg,#b08a6a,#5d4637)}
.stars{color:var(--orange);font-size:11px;letter-spacing:1px}
.quote-name{font-size:11px;line-height:18px;color:var(--white);margin-top:2px}
.quote-text{font-size:11px;line-height:19px;color:#d8d8d8;margin-top:26px}
.slider-arrow{width:32px;height:32px;border-radius:50%;background:var(--orange);display:flex;align-items:center;justify-content:center}

/* intro */
.video-frame{left:288px;top:4340px;width:624px;height:308px;background:linear-gradient(135deg,#1c4d72,#0f3556 60%,#14405f)}
.agent-bar{left:288px;top:4730px;width:624px;height:72px;background:var(--navy)}
.agent-bar .field{position:absolute;top:33px;font-size:11px;color:var(--white);border-bottom:1px solid var(--white);padding-bottom:3px}

/* footer */
.site-footer{left:0;top:4870px;width:1200px;height:356px;background:var(--footer);color:var(--white)}
.footer-col h4{font-family:"League Spartan",sans-serif;font-size:15px;font-weight:600;color:var(--orange);letter-spacing:.5px}
.footer-col a,.footer-col p{display:block;font-size:10.5px;color:var(--white);text-decoration:none;margin-top:22px}
.social{width:16px;height:16px;background:var(--white);border-radius:2px}
.legal{font-size:8px;color:#ddd}
</style>
</head>
<body>

<header class="abs site-header">
  <div class="abs brand" style="left:228px;top:18px">
    <span class="brand-dot"></span>
    <span>MILEPOST<br>INSURANCE</span>
  </div>
  <nav class="main-nav">
    <a class="active" href="#" style="left:485px">Home</a>
    <a href="#" style="left:546px">About Us</a>
    <a href="#" style="left:628px">Insurances</a>
    <a href="#" style="left:721px">Contact Us</a>
  </nav>
  <a class="abs btn btn-solid" href="#" style="left:833px;top:20px;width:142px;height:35px">Get a Quote</a>
</header>

<section class="abs hero">
  <svg width="1200" height="522" class="abs" style="left:0;top:0">
    <defs>
      <linearGradient id="warehouseTone" x1="0" y1="0" x2="1" y2="1">
        <stop offset="0" stop-color="#1a4f78"/>
        <stop offset="1" stop-color="#0a2f4d"/>
      </linearGradient>
      <linearGradient id="driverTone" x1="0" y1="0" x2="1" y2="1">
        <stop offset="0" stop-color="#e9e6e1"/>
        <stop offset=".55" stop-color="#b9a38c"/>
        <stop offset="1" stop-color="#6a7580"/>
      </linearGradient>
    </defs>
    <rect width="1200" height="522" fill="url(#warehouseTone)" role="img" aria-label="Warehouse shelving in a blue tint"/>
    <path d="M0 0 H608 Q680 270 480 522 H0 Z" fill="url(#driverTone)" role="img" aria-label="Smiling truck driver with crossed arms in front of a white truck"/>
    <path d="M608 0 Q680 270 480 522" fill="none" stroke="#fff" stroke-width="4"/>
  </svg>
  <h1 class="abs hero-title">Insurance<br><span class="accent">Solutions</span> for the<br>Trucking Industry</h1>
  <p class="abs hero-sub">Comprehensive Insurance Solutions for Trucking Companies</p>
  <a class="abs btn btn-solid" href="#" style="left:666px;top:337px;width:140px;height:36px">Get a Quote</a>
  <a class="abs btn btn-ghost" href="#" style="left:826px;top:337px;width:138px;height:36px">Learn More</a>
</section>

<section class="abs stats">
  <div class="stat" style="left:225px"><b>12+</b><span>Years of Experience</span></div>
  <div class="stat" style="left:438px"><b>23</b><span>Agencies, Worked with</span></div>
  <div class="stat" style="left:672px"><b>10k+</b><span>Truck Insurances</span></div>
  <div class="stat" style="left:868px"><b>100%</b><span>Satisfaction Rate</span></div>
</section>

<section class="abs about">
  <h2 class="section-title" style="margin-top:64px">About <span class="accent">Us</span></h2>
  <p>At Milepost Insurance, we are dedicated to providing comprehensive insurance solutions specifically tailored to the unique needs of the trucking industry. As a trusted and reliable partner, we understand the challenges and risks faced by trucking businesses, and we are committed to helping them navigate the complexities of insurance with confidence and ease.</p>
</section>

<section class="abs services-head">
  <h2 class="section-title">Our <span class="accent">Insurance</span> Services</h2>
  <p class="section-sub">Comprehensive Coverage Tailored to Your Trucking Business</p>
</section>

<!-- service rows -->
<div class="abs" style="left:225px;top:1188px"><h3 class="service-title">Liability Insurance</h3><p class="service-desc">Coverage for bodily injury and property damage liability, protecting trucking businesses from potential lawsuits and financial risks.</p></div>
<div class="abs service-photo" style="left:606px;top:1154px;background:linear-gradient(135deg,#8a5a34,#c49a72 50%,#7a4d2c)" role="img" aria-label="Hand writing in a notebook on a wooden desk"></div>
<div class="abs service-count" style="left:606px;top:1317px">1/6</div>

<div class="abs service-photo" style="left:225px;top:1373px;background:linear-gradient(135deg,#4a6fa0,#c9b69a 55%,#8fa7c4)" role="img" aria-label="Hands stacking coins on a table"></div>
<div class="abs service-count" style="left:575px;top:1536px">2/6</div>
<div class="abs" style="left:672px;top:1407px"><h3 class="service-title">Cargo Insurance</h3><p class="service-desc">Protection for the goods and cargo being transported, covering losses or damages that may occur during transit.</p></div>

<div class="abs" style="left:225px;top:1626px"><h3 class="service-title">Owner-Operator Insurance</h3><p class="service-desc">Tailored insurance solutions designed specifically for independent truck drivers, addressing their unique needs and risks.</p></div>
<div class="abs service-photo" style="left:606px;top:1592px;background:linear-gradient(135deg,#3d4752,#b3b6ba 50%,#2c2f35)" role="img" aria-label="Two businessmen shaking hands"></div>
<div class="abs service-count" style="left:606px;top:1755px">3/6</div>

<div class="abs service-photo" style="left:225px;top:1811px;background:linear-gradient(135deg,#5c7aa3,#d5dbe3 55%,#7d8ea3)" role="img" aria-label="People reviewing documents beside a laptop"></div>
<div class="abs service-count" style="left:575px;top:1974px">4/6</div>
<div class="abs" style="left:672px;top:1845px"><h3 class="service-title">Commercial Auto Insurance</h3><p class="service-desc">Protection for commercial vehicles beyond just liability coverage, encompassing comprehensive, collision, and other relevant coverages.</p></div>

<div class="abs" style="left:225px;top:2064px"><h3 class="service-title">General Liability Insurance</h3><p class="service-desc">Broad coverage for various liability risks faced by trucking businesses, including premises liability, product liability, and completed operations liability.</p></div>
<div class="abs service-photo" style="left:606px;top:2030px;background:linear-gradient(135deg,#e8e4dc,#9b8470 50%,#d9d4cb)" role="img" aria-label="Colleagues giving a high five in an office"></div>
<div class="abs service-count" style="left:606px;top:2193px">5/6</div>

<div class="abs service-photo" style="left:225px;top:2249px;background:linear-gradient(135deg,#c9955c,#e6d9c6 50%,#b68550)" role="img" aria-label="Team planning with notes and a phone on a desk"></div>
<div class="abs service-count" style="left:575px;top:2412px">6/6</div>
<div class="abs" style="left:672px;top:2283px"><h3 class="service-title">Bobtail Insurance</h3><p class="service-desc">Insurance coverage for non-trucking use or instances when the truck is not hauling any cargo, providing liability protection during these periods</p></div>

<section class="abs claims">
  <div class="abs center-head" style="top:66px">
    <h2 class="section-title">Claims <span class="accent">Process</span> and Support</h2>
    <p class="section-sub">Comprehensive Coverage Tailored to Your Trucking Business</p>
  </div>

  <div class="abs claim-card" style="left:225px;top:177px">
    <svg width="30" height="30" viewBox="0 0 30 30"><rect x="5" y="3" width="18" height="24" rx="2" fill="none" stroke="#ff5a0a" stroke-width="2.5"/><path d="M9 10h10M9 15h10M9 20h6" stroke="#ff5a0a" stroke-width="2"/></svg>
    <h3>Reporting a Claim</h3>
    <p>When an incident occurs, promptly report the claim to our dedicated claims department.</p>
    <p>You can reach us through our 24/7 claims hotline or by submitting a claim online through our user-friendly portal.</p>
    <p>Our team is ready to guide you through the process and provide the necessary support.</p>
  </div>
  <div class="abs claim-card featured" style="left:479px;top:177px">
    <svg width="30" height="30" viewBox="0 0 30 30"><circle cx="13" cy="9" r="6" fill="#ff5a0a"/><path d="M2 28c0-7 5-11 11-11s11 4 11 11z" fill="#ff5a0a"/></svg>
    <h3>Personalized Assistance</h3>
    <p>Our knowledgeable claims professionals will work closely with you, providing personalized assistance throughout the entire claims process.</p>
    <p>We will guide you through the necessary documentation, answer your questions, and address any concerns you may have.</p>
    <p>We are committed to keeping you informed and involved at every step.</p>
  </div>
  <div class="abs claim-card" style="left:733px;top:177px">
    <svg width="30" height="30" viewBox="0 0 30 30"><circle cx="12" cy="12" r="8" fill="none" stroke="#ff5a0a" stroke-width="3"/><path d="M18 18l9 9" stroke="#ff5a0a" stroke-width="4" stroke-linecap="round"/></svg>
    <h3>Expert Evaluation</h3>
    <p>Our claims adjusters have in-depth knowledge of the trucking industry and understand the intricacies involved in assessing damages.</p>
    <p>We will conduct a thorough evaluation of the situation, considering all relevant factors to determine the coverage and benefits you are entitled to.</p>
  </div>
  <div class="abs claim-card" style="left:352px;top:567px">
    <svg width="30" height="30" viewBox="0 0 30 30"><rect x="2" y="4" width="26" height="24" fill="#ff5a0a"/><rect x="5" y="11" width="20" height="14" fill="#fff"/><text x="15" y="23" text-anchor="middle" font-family="League Spartan,sans-serif" font-weight="700" font-size="11" fill="#ff5a0a">23</text></svg>
    <h3>Timely Resolution</h3>
    <p>We strive to expedite the claims process and achieve a fair and timely resolution.</p>
    <p>Our team will work diligently to negotiate with all parties involved and handle any necessary paperwork, aiming to resolve your claim efficiently</p>
  </div>
  <div class="abs claim-card" style="left:606px;top:567px">
    <svg width="30" height="30" viewBox="0 0 30 30"><path d="M15 3v24M8 27h14M4 8h22" stroke="#ff5a0a" stroke-width="2.5"/><path d="M4 8l-4 9h8zM26 8l-4 9h8z" fill="#ff5a0a"/></svg>
    <h3>Advocacy and Support</h3>
    <p>As your dedicated insurance partner, we are here to advocate for you throughout the claims process.</p>
    <p>We will represent your best interests and work diligently to achieve a fair resolution.</p>
    <p>Our team is committed to providing the support you need, ensuring you receive the benefits and coverage you are entitled to.</p>
  </div>
</section>

<section class="abs testimonials">
  <div class="abs" style="left:760px;top:0;width:440px;height:625px;background:linear-gradient(90deg,#1a1a1a,#4a4a48 40%,#b29c86 75%,#d8c9b8)" role="img" aria-label="Woman smiling while working on a laptop"></div>
  <div class="abs" style="left:225px;top:72px">
    <h2 class="section-title" style="color:#fff">What Our <span class="accent">Clients</span> Say</h2>
    <p class="section-sub" style="color:#ddd">Words of Appreciation from Our Clients</p>
  </div>
  <div class="abs quote-card" style="left:0;width:70px;padding:0"></div>
  <div class="abs quote-card" style="left:90px;width:350px">
    <div style="display:flex;gap:18px;align-items:center">
      <div class="quote-avatar" role="img" aria-label="Client portrait"></div>
      <div><div class="stars">★★★★★</div><div class="quote-name">Clara Benson, Owner of<br>Ridgeway Freight</div></div>
    </div>
    <p class="quote-text">Milepost Insurance has been an invaluable partner in protecting my trucking business. Their comprehensive coverage options and personalized service have given me peace of mind on the road. Their claims team is responsive and efficient, making the process hassle-free.</p>
  </div>
  <div class="abs quote-card" style="left:460px;width:352px">
    <div style="display:flex;gap:18px;align-items:center">
      <div class="quote-avatar" role="img" aria-label="Client portrait"></div>
      <div><div class="stars">★★★★★</div><div class="quote-name">Dana Whitfield, Trucking<br>Industry Professional</div></div>
    </div>
    <p class="quote-text">Milepost Insurance is a reliable partner with exceptional service. Their tailored insurance solutions for the trucking industry are unmatched. They understand our unique challenges and deliver personalized attention. I highly recommend Milepost Insurance to fellow industry professionals.</p>
  </div>
  <div class="abs slider-arrow" style="left:224px;top:511px"><svg width="14" height="14" viewBox="0 0 14 14"><path d="M12 7H2M6 3L2 7l4 4" stroke="#fff" stroke-width="2" fill="none"/></svg></div>
  <div class="abs" style="left:274px;top:524px;display:flex;gap:5px"><span style="width:7px;height:7px;border-radius:50%;background:#fff"></span><span style="width:7px;height:7px;border-radius:50%;background:#fff"></span><span style="width:7px;height:7px;border-radius:50%;background:var(--orange)"></span></div>
  <div class="abs slider-arrow" style="left:326px;top:511px"><svg width="14" height="14" viewBox="0 0 14 14"><path d="M2 7h10M8 3l4 4-4 4" stroke="#fff" stroke-width="2" fill="none"/></svg></div>
</section>

<div class="abs center-head" style="top:4216px">
  <h2 class="section-title">Introducing <span class="accent">Milepost</span> Insurance</h2>
  <p class="section-sub">Embracing the Milepost Insurance Spirit: Team Bonding and Camaraderie</p>
</div>
<div class="abs video-frame" role="img" aria-label="Video still of a warehouse in blue tones">
  <svg class="abs" style="left:276px;top:118px" width="72" height="72" viewBox="0 0 72 72"><circle cx="36" cy="36" r="34" fill="none" stroke="#fff" stroke-width="2"/><path d="M30 25l16 11-16 11z" fill="#fff"/></svg>
</div>
<div class="abs agent-bar">
  <div class="abs display" style="left:30px;top:20px;color:#fff;font-size:14px;font-weight:700;line-height:17px">Find an <span class="accent">agent</span><br>near You</div>
  <svg class="abs" style="left:176px;top:31px" width="10" height="14" viewBox="0 0 10 14"><path d="M5 0a5 5 0 0 1 5 5c0 4-5 9-5 9S0 9 0 5a5 5 0 0 1 5-5z" fill="#fff"/><circle cx="5" cy="5" r="2" fill="#0c3b60"/></svg>
  <div class="field" style="left:176px;width:138px;padding-left:18px">Enter Your Zip Code</div>
  <div class="field" style="left:336px;width:134px">Select an Insurance <span style="float:right;font-size:8px">▼</span></div>
  <a class="abs btn btn-solid" href="#" style="left:500px;top:19px;width:94px;height:36px">Find</a>
</div>

<footer class="abs site-footer">
  <div class="abs brand" style="left:233px;top:90px;color:var(--orange)">
    <span class="brand-dot" style="background:var(--orange)"></span>
    <span>MILEPOST<br>INSURANCE</span>
  </div>
  <div class="abs" style="left:268px;top:158px;display:flex;gap:12px"><span class="social"></span><span class="social"></span></div>
  <div class="abs footer-col" style="left:433px;top:70px">
    <h4>NAVIGATIONS</h4>
    <a href="#" style="margin-top:28px">Home</a><a href="#">About Us</a><a href="#">Insurances</a><a href="#">Contact Us</a>
  </div>
  <div class="abs footer-col" style="left:621px;top:70px">
    <h4>INSURANCES</h4>
    <a href="#" style="margin-top:28px">Cargo Insurance</a><a href="#">Bobtail Insurance</a><a href="#">Liability Insurance</a><a href="#">Commercial Auto Insurance</a>
  </div>
  <div class="abs footer-col" style="left:835px;top:70px;width:140px">
    <h4>SUPPORT</h4>
    <p style="margin-top:28px">Phone No. (209) 555 0143</p>
    <p>Email: hello@milepostins.com</p>
    <h4 style="margin-top:28px">NEWSLETTER</h4>
    <div style="margin-top:18px;height:24px;background:#fff;font-size:8px;color:#555;padding:7px 10px">Enter Email</div>
    <a class="btn btn-solid" href="#" style="margin-top:12px;height:30px">Submit</a>
  </div>
  <div class="abs legal" style="left:225px;top:336px">All Rights Reserved</div>
  <div class="abs legal" style="left:550px;top:336px">© 2023, Milepost Insurance</div>
  <div class="abs legal" style="left:858px;top:336px">Terms Conditions | Privacy &amp; Policy</div>
</footer>

</body>
</html>
```